Flyer for Harbourline Accounting & Taxation, a local tax practice

Flyer for my business to be distributed locally in the Western Suburb of Melbourne (Size: DL, Fold: Flat, Backside: Blank) This will include below information (Font, color and capitalization of the text is for the designer's creativity):
Harbourline Accounting & Taxation Your Local Tax Accountant
ABN: 37 481 259 604
Address: 9 Marlo Place, Wattle Bend
kolvend@hbatx.com.au
Call Tobias on 0419 786 205 to book your appointment
Services we offer:
Individual & Company Tax Returns
Company & Trust formation
Business Advisory
Bookkeeping
BAS & IAS
Payroll
TPAR
Please include the logo of the business attached which was designed by PixelForum few years ago.
Please include the NBF, RCQ and Lumo logos somewhere in the bottom, preferable the same size and aligned (attached)

```html
<!DOCTYPE html>
<html lang="en">
<head>
<meta charset="utf-8">
<title>Harbourline Accounting &amp; Taxation – Flyer</title>
<link rel="stylesheet" href="https://fonts.googleapis.com/css2?family=Montserrat:wght@500;600;700&display=swap">
<style>
  :root{
    --orange:#ee7230;
    --charcoal:#3c3c41;
    --paper:#f5f5f3;
    --white:#ffffff;
    --photo-warm:#c99a78;
    --photo-dark:#4a423e;
    --photo-light:#e9eef3;
    --badge-neutral:#d4d6da;
  }
  *{box-sizing:border-box;margin:0;padding:0}
  html,body{width:831px;height:1200px;overflow:hidden;background:#b9bcc2}
  body{font-family:'Montserrat',sans-serif}
  .flyer{position:relative;width:831px;height:1200px;background:var(--paper);overflow:hidden}
  .hero-photo{position:absolute;left:0;top:0;width:831px;height:418px;
    background:linear-gradient(110deg,var(--photo-dark) 0%,#7a5a48 22%,var(--photo-warm) 45%,#dcc3b0 65%,var(--photo-light) 100%)}
  .hero-brand{position:absolute;right:32px;top:262px;display:flex;align-items:center;gap:10px}
  .hero-brand .mark-square{flex:none;width:16px;height:16px;background:var(--orange)}
  .hero-brand span{font-weight:600;font-size:18px;line-height:22px;color:var(--charcoal)}
  .band{position:absolute;top:418px;left:0;width:831px;height:15px;
    background:linear-gradient(90deg,var(--orange) 0 116px,var(--charcoal) 116px 712px,var(--orange) 712px)}
  .masthead{position:absolute;top:470px;left:86px;width:680px;height:80px}
  .brand{position:absolute;left:0;top:6px;width:290px;display:flex;align-items:center;gap:12px}
  .brand .mark-square{flex:none;width:20px;height:20px;background:var(--orange)}
  .brand-name{font-weight:600;font-size:20px;line-height:25px;color:var(--charcoal);white-space:nowrap}
  .divider{position:absolute;left:334px;top:0;width:1px;height:64px;background:var(--charcoal)}
  .tagline{position:absolute;left:356px;top:-6px;font-weight:700;font-size:29px;line-height:36px;color:var(--charcoal)}
  .tagline .accent{color:var(--orange)}
  .services-title{position:absolute;top:585px;left:0;width:831px;height:46px}
  .services-title .rule{position:absolute;top:22px;height:1.5px;background:var(--orange)}
  .services-title .pill{position:absolute;left:259px;top:0;width:310px;height:46px;border:1.5px solid var(--orange);border-radius:23px;
    color:var(--orange);font-weight:700;font-size:23px;line-height:43px;text-align:center;letter-spacing:.3px}
  .service{position:absolute;display:flex;align-items:center;font-weight:700;font-size:18.5px;line-height:23px;color:var(--charcoal);text-transform:uppercase}
  .service svg{position:absolute;width:40px;height:44px}
  .partners{position:absolute;top:932px;left:0;width:831px;height:60px}
  .footer{position:absolute;left:0;top:1035px;width:831px;height:165px}
  .footer-bg{position:absolute;left:0;top:0}
  .contact{position:absolute;left:69px;top:22px;color:var(--white);font-weight:500;font-size:15px}
  .contact .abn{font-weight:600}
  .contact .abn b{font-weight:700}
  .contact .rule{width:147px;height:1.5px;background:var(--orange);margin:8px 0 9px}
  .contact p{line-height:22px;position:relative}
  .contact .icon{position:absolute;left:-22px;top:4px}
  .cta{position:absolute;left:480px;top:30px;width:330px;text-align:center;font-weight:700}
  .cta .call{color:var(--white);font-size:19px;display:flex;align-items:center;justify-content:center;gap:8px}
  .cta .number{color:var(--white);font-size:32px;letter-spacing:4.5px;margin-top:2px}
  .cta .book{color:var(--charcoal);font-size:15.5px;margin-top:2px}
</style>
</head>
<body>
<main class="flyer">
  <div class="hero-photo" role="img" aria-label="Photo of an accountant's hand with a pen reviewing financial charts beside a calculator"></div>
  <div class="hero-brand"><div class="mark-square"></div><span>Harbourline<br>Accounting &amp; Taxation</span></div>
  <div class="band"></div>

  <header class="masthead">
    <div class="brand"><div class="mark-square"></div><div class="brand-name">Harbourline<br>Accounting &amp; Taxation</div></div>
    <div class="divider"></div>
    <h1 class="tagline">YOUR LOCAL<br><span class="accent">TAX ACCOUNTANT</span></h1>
  </header>

  <section class="services-title">
    <div class="rule" style="left:50px;width:196px"></div>
    <h2 class="pill">SERVICES WE OFFER:</h2>
    <div class="rule" style="left:586px;width:214px"></div>
  </section>

  <div class="service" style="left:186px;top:675px">
    <svg style="left:-66px;top:-2px" viewBox="0 0 40 44" fill="none" stroke-width="1.4">
      <rect x="5" y="4" width="28" height="34" rx="3" stroke="var(--orange)"/>
      <text x="19" y="14" font-family="Montserrat,sans-serif" font-size="8" font-weight="600" fill="var(--charcoal)" stroke="none" text-anchor="middle">TAX</text>
      <path d="M10 21h18M10 26h18M10 31h18" stroke="var(--charcoal)"/>
    </svg>
    <span>Individual &amp; Company<br>Tax Returns</span>
  </div>
  <div class="service" style="left:186px;top:770px">
    <svg style="left:-66px;top:-2px" viewBox="0 0 40 44" fill="none" stroke-width="1.4">
      <path d="M19 4l14 5v12c0 9-6 15-14 19C11 36 5 30 5 21V9z" stroke="var(--orange)"/>
      <path d="M12 21l5 6 12-16" stroke="var(--charcoal)"/>
    </svg>
    <span>Company &amp; Trust<br>Formation</span>
  </div>
  <div class="service" style="left:186px;top:864px">
    <svg style="left:-66px;top:-12px" viewBox="0 0 40 44" fill="none" stroke-width="1.4">
      <path d="M6 12h28a2 2 0 0 1 2 2v14a2 2 0 0 1-2 2H23l-4 4-4-4H6a2 2 0 0 1-2-2V14a2 2 0 0 1 2-2z" stroke="var(--orange)"/>
      <circle cx="13" cy="21" r="2" stroke="var(--charcoal)"/><circle cx="20" cy="21" r="2" stroke="var(--charcoal)"/><circle cx="27" cy="21" r="2" stroke="var(--charcoal)"/>
    </svg>
    <span>Business Advisory</span>
  </div>

  <div class="service" style="left:547px;top:676px">
    <svg style="left:-66px;top:-14px" viewBox="0 0 40 44" fill="none" stroke-width="1.4">
      <path d="M8 4h24v30H8z" stroke="var(--charcoal)"/>
      <path d="M8 34c-3 0-3 5 0 5h26" stroke="var(--orange)"/>
      <path d="M12 36v6l2-2 2 2v-6" stroke="var(--orange)"/>
      <text x="20" y="18" font-family="Montserrat,sans-serif" font-size="11" fill="var(--charcoal)" stroke="none" text-anchor="middle">$</text>
    </svg>
    <span>Bookkeeping</span>
  </div>
  <div class="service" style="left:547px;top:738px">
    <svg style="left:-66px;top:-8px" viewBox="0 0 40 44" fill="none" stroke-width="1.4">
      <path d="M9 6h24v34H13l-4-4z" stroke="var(--orange)"/>
      <path d="M14 15h15M14 20h15M14 25h15M14 30h15" stroke="var(--charcoal)"/>
      <circle cx="8" cy="6" r="4.5" stroke="var(--orange)" fill="var(--paper)"/>
      <text x="8" y="9" font-family="Montserrat,sans-serif" font-size="7" fill="var(--charcoal)" stroke="none" text-anchor="middle">$</text>
    </svg>
    <span>BAS &amp; IAS</span>
  </div>
  <div class="service" style="left:547px;top:801px">
    <svg style="left:-66px;top:-12px" viewBox="0 0 40 44" fill="none" stroke-width="1.4">
      <path d="M8 24V4h24v20" stroke="var(--orange)"/>
      <path d="M13 10h14M13 14h14" stroke="var(--charcoal)"/>
      <rect x="6" y="22" width="28" height="18" stroke="var(--charcoal)"/>
      <path d="M6 22l14 10 14-10M6 40l10-9M34 40l-10-9" stroke="var(--charcoal)"/>
    </svg>
    <span>Payroll</span>
  </div>
  <div class="service" style="left:547px;top:863px">
    <svg style="left:-66px;top:-12px" viewBox="0 0 40 44" fill="none" stroke-width="1.4">
      <path d="M10 4h24v34l-4 4H10z" stroke="var(--orange)"/>
      <path d="M6 10h6M6 18h6M6 26h6M6 34h6" stroke="var(--orange)"/>
      <path d="M16 30l5-6 4 3 6-8M28 19h3v3" stroke="var(--charcoal)"/>
      <text x="21" y="17" font-family="Montserrat,sans-serif" font-size="10" fill="var(--charcoal)" stroke="none" text-anchor="middle">$</text>
    </svg>
    <span>TPAR</span>
  </div>

  <section class="partners" aria-label="Partner and registration badges">
    <svg width="831" height="60" viewBox="0 0 831 60">
      <rect x="293" y="4" width="52" height="52" rx="8" fill="var(--badge-neutral)"/>
      <rect x="390" y="4" width="52" height="52" rx="8" fill="var(--badge-neutral)"/>
      <rect x="487" y="4" width="52" height="52" rx="8" fill="var(--badge-neutral)"/>
    </svg>
  </section>

  <footer class="footer">
    <svg class="footer-bg" width="831" height="165" viewBox="0 0 831 165">
      <rect width="831" height="165" fill="var(--orange)"/>
      <path d="M0 0H516C470 8 440 40 400 84C370 116 350 128 300 128H0Z" fill="var(--charcoal)"/>
      <path d="M0 132H302C354 132 376 118 406 86C444 44 474 12 520 2" fill="none" stroke="var(--white)" stroke-width="3"/>
    </svg>
    <div class="contact">
      <div class="abn"><b>ABN:</b> 37 481 259 604</div>
      <div class="rule"></div>
      <p><svg class="icon" width="14" height="16" viewBox="0 0 14 16" fill="none" stroke="var(--orange)" stroke-width="1.3"><path d="M7 15S1.5 9.5 1.5 6a5.5 5.5 0 0 1 11 0C12.5 9.5 7 15 7 15z"/><circle cx="7" cy="6" r="2"/></svg>9 MARLO PLACE, WATTLE BEND</p>
      <p><svg class="icon" width="16" height="12" viewBox="0 0 16 12" fill="none" stroke="var(--orange)" stroke-width="1.3"><rect x="1" y="1" width="14" height="10"/><path d="M1 1l7 6 7-6M1 11l5-5M15 11l-5-5"/></svg>KOLVEND@HBATX.COM.AU</p>
    </div>
    <div class="cta">
      <div class="call"><svg width="20" height="20" viewBox="0 0 24 24"><path d="M6.6 10.8a15.1 15.1 0 0 0 6.6 6.6l2.2-2.2a1 1 0 0 1 1-.25 11.4 11.4 0 0 0 3.6.57 1 1 0 0 1 1 1V20a1 1 0 0 1-1 1A17 17 0 0 1 3 4a1 1 0 0 1 1-1h3.5a1 1 0 0 1 1 1c0 1.25.2 2.45.57 3.57a1 1 0 0 1-.25 1z" fill="var(--charcoal)"/></svg>CALL TOBIAS ON</div>
      <div class="number">0419 786 205</div>
      <div class="book">TO BOOK YOUR APPOINTMENT</div>
    </div>
  </footer>
</main>
</body>
</html>
```